Business Card Design Project

Looking for a business card that our customers will remember. We are a high end Travel Agency.
Need a re-memorable classy business card.
Both sides full color.
Must have the following details.
Voyage Harbor Logo (see attached)
4B Wattle Lane
Penhurst Sydney NSW 2241
Phone: 02 9471 3652
Fax: 02 9563 4417
sales@voyageharbor-example.com.au
Consultant Name
Anything else you think we need

```html
<!DOCTYPE html>
<html lang="en">
<head>
<meta charset="utf-8">
<title>Voyage Harbor Business Card</title>
<link rel="stylesheet" href="https://fonts.googleapis.com/css2?family=Dosis:wght@500;600&display=swap">
<style>
  :root {
    --stage: #2b2b2b;
    --yellow: #f7c51a;
    --blue: #1f5a85;
    --black: #111111;
    --white: #ffffff;
    --ink: #1a1a1a;
    --mist: rgba(215, 215, 215, 0.55);
    --mist-clear: rgba(215, 215, 215, 0);
  }
  * { margin: 0; padding: 0; box-sizing: border-box; }
  html, body {
    width: 1200px; height: 900px; overflow: hidden;
    background: var(--stage);
    font-family: "Dosis", "Arial Narrow", sans-serif;
  }
  .sheet {
    width: 1200px; height: 900px;
    display: flex; flex-direction: column; align-items: center; justify-content: center;
    gap: 44px;
  }
  .card {
    position: relative; width: 620px; height: 380px; overflow: hidden;
    background: var(--white);
  }
  .card svg.art { position: absolute; inset: 0; }
  .brand-text { font-family: "Dosis", "Arial Narrow", sans-serif; font-weight: 600; fill: var(--blue); }
  .web-text { font-family: "Dosis", "Arial Narrow", sans-serif; font-weight: 500; fill: var(--ink); letter-spacing: 3px; }

  /* contact side */
  .decor-area {
    position: absolute; left: 290px; top: 50px; width: 290px; height: 220px;
    background: radial-gradient(ellipse at 55% 45%, var(--mist) 0%, var(--mist-clear) 70%);
  }
  .brand {
    position: absolute; left: 40px; top: 48px;
    display: flex; align-items: center; gap: 10px;
    font-weight: 600; font-size: 34px; color: var(--blue); letter-spacing: 1px;
  }
  .brand-dot { width: 12px; height: 12px; border-radius: 50%; background: var(--yellow); }
  .holder { position: absolute; right: 42px; top: 112px; text-align: right; }
  .holder-name { font-size: 21px; font-weight: 600; color: var(--blue); letter-spacing: 1px; }
  .holder-role { font-size: 15px; font-weight: 500; color: var(--ink); }
  .tab {
    position: absolute; right: 0; top: 106px; width: 18px; height: 30px;
    background: var(--black); border-radius: 6px 0 0 6px;
  }
  .contact { position: absolute; font-size: 17px; font-weight: 500; color: var(--ink); line-height: 1.3; }
  .address { left: 40px; top: 208px; }
  .phones { left: 40px; top: 266px; }
  .online { left: 254px; top: 230px; }
  .label { color: var(--yellow); margin-right: 4px; }
  .bar { position: absolute; }
  .bar-black { left: 0; top: 344px; width: 200px; height: 36px; background: var(--black); }
  .bar-yellow-a { left: 200px; top: 320px; width: 38px; height: 60px; background: var(--yellow); }
  .bar-blue { left: 238px; top: 320px; width: 190px; height: 60px; background: var(--blue); }
  .bar-yellow-b { left: 428px; top: 290px; width: 192px; height: 90px; background: var(--yellow); }
</style>
</head>
<body>
<main class="sheet">

  <section class="card card-logo-side" aria-label="Card front">
    <svg class="art" viewBox="0 0 620 380" width="620" height="380">
      <defs><clipPath id="card-edge"><rect width="620" height="380"/></clipPath></defs>
      <g clip-path="url(#card-edge)">
        <polygon points="0,0 620,0 620,30 0,230" fill="var(--yellow)"/>
        <polygon points="0,230 620,30 620,45 0,245" fill="var(--blue)"/>
        <polygon points="0,245 620,45 620,245 0,445" fill="var(--white)"/>
        <polygon points="0,445 620,245 620,325 0,525" fill="var(--yellow)"/>
        <polygon points="0,525 620,325 620,380 0,380" fill="var(--black)"/>
        <g transform="translate(300 250) rotate(-17.9)">
          <circle cx="-150" cy="-11" r="7" fill="var(--yellow)"/>
          <text class="brand-text" x="-132" y="0" font-size="36">Voyage Harbor</text>
        </g>
        <g transform="translate(430 330) rotate(-17.9)">
          <text class="web-text" x="-120" y="5" font-size="14">www.voyageharbor-example.com.au</text>
        </g>
      </g>
    </svg>
  </section>

  <section class="card card-contact-side" aria-label="Card back">
    <div class="decor-area" role="img" aria-label="Faint large aircraft illustration belongs here"></div>
    <div class="brand"><span class="brand-dot"></span><span>Voyage Harbor</span></div>
    <div class="holder">
      <p class="holder-name">DANIEL WHITFORD</p>
      <p class="holder-role">Manager</p>
    </div>
    <div class="tab"></div>
    <p class="contact address">4B Wattle Lane<br>Penhurst Sydney NSW 2241</p>
    <p class="contact phones"><span class="label">P:</span>02 9471 3652<br><span class="label">F:</span>02 9563 4417</p>
    <p class="contact online"><span class="label">E:</span>sales@voyageharbor-example.com.au<br><span class="label">W:</span>www.voyageharbor-example.com.au</p>
    <div class="bar bar-black"></div>
    <div class="bar bar-yellow-a"></div>
    <div class="bar bar-blue"></div>
    <div class="bar bar-yellow-b"></div>
  </section>

</main>
</body>
</html>
```